Book cover "Beyond the quiet"

Creation of a cover with three submitted images The book is an autobiography of a man who stayed three years hided in an attic with his parents to escape from the Germans soldiers during the II World War. Author: Tomas Veldrin Title: Beyond the quiet SubTitle (not very important): Tomas et l% 26 # 39; ing% 26 # 233; nieur Publishers (with Gill sans Light Font): Editions Marvolt 16 x 24 cm
Updates

Besoin de quelques jours pour choisir un design

Besoin de plus de jours pour examiner

Target Market(s)

General public (adults)

Colors

Designer to choose colors to be used in the design.

Requirements
Must have
• The three joined images

```html
<!DOCTYPE html>
<html lang="en">
<head>
<meta charset="utf-8">
<title>Beyond the Quiet — Tomas Veldrin</title>
<link rel="stylesheet" href="https://fonts.googleapis.com/css2?family=Josefin+Sans:wght@300;400&display=swap">
<style>
  :root {
    --page-bg: #e8e8e8;
    --cover-black: #050303;
    --cover-red: #8e0a0c;
    --cover-red-deep: #4a0406;
    --title-white: #f4f1ec;
    --paper-cream: #ecefdf;
    --paper-shadow: #8c8f9c;
    --photo-grey: #6e6b68;
    --photo-grey-dark: #3a3836;
    --portrait-grey: #8d8b89;
  }
  * { box-sizing: border-box; margin: 0; padding: 0; }
  html, body {
    width: 1200px;
    height: 800px;
    overflow: hidden;
    background: var(--page-bg);
  }
  .book-cover {
    position: absolute;
    left: 360px;
    top: 34px;
    width: 480px;
    height: 732px;
    background: var(--cover-black);
    overflow: hidden;
    font-family: "Josefin Sans", "Gill Sans", sans-serif;
    font-weight: 300;
    color: var(--title-white);
    text-transform: uppercase;
    text-align: center;
  }
  .cover-backdrop {
    position: absolute;
    inset: 0;
    background:
      radial-gradient(ellipse 70% 45% at 45% 55%, rgba(142,10,12,0.85), rgba(142,10,12,0) 75%),
      linear-gradient(180deg, var(--cover-black) 0%, var(--cover-black) 14%, var(--cover-red-deep) 40%, var(--cover-red) 70%, var(--cover-red-deep) 100%);
  }
  .cover-text { position: absolute; left: 0; width: 100%; line-height: 1; }
  .author-name { top: 30px; font-size: 31px; letter-spacing: 0.14em; padding-left: 0.14em; }
  .title-line-1 { top: 146px; font-size: 78px; letter-spacing: 0.08em; padding-left: 0.08em; }
  .title-line-2 { top: 232px; font-size: 48px; letter-spacing: 0.1em; padding-left: 0.1em; }
  .title-line-3 { top: 294px; font-size: 72px; letter-spacing: 0.08em; padding-left: 0.08em; }
  .subtitle { top: 370px; font-size: 40px; letter-spacing: 0.1em; padding-left: 0.1em; }
  .photo-strip { position: absolute; left: 0; top: 448px; width: 480px; height: 250px; }
  .attic-photo {
    position: absolute; left: 0; top: 24px; width: 340px; height: 202px;
    background: linear-gradient(180deg, var(--photo-grey-dark) 0%, var(--photo-grey) 60%, #a9a6a1 100%);
  }
  .portrait-photo {
    position: absolute; left: 343px; top: 30px; width: 132px; height: 188px;
    background: linear-gradient(180deg, #a3a19f 0%, var(--portrait-grey) 55%, #4d4b4a 100%);
    transform: rotate(-2deg);
  }
  .publisher-name { top: 705px; font-size: 17px; letter-spacing: 0.16em; padding-left: 0.16em; font-weight: 300; }
</style>
</head>
<body>
  <main class="book-cover">
    <div class="cover-backdrop" role="img" aria-label="Red-toned view of a gothic church and old town rooftops at night"></div>

    <p class="cover-text author-name">Tomas Veldrin</p>
    <h1 class="book-title">
      <span class="cover-text title-line-1">Beyond</span>
      <span class="cover-text title-line-2">the</span>
      <span class="cover-text title-line-3">Quiet</span>
    </h1>
    <p class="cover-text subtitle">Tomas et</p>

    <div class="photo-strip">
      <svg class="torn-paper" width="480" height="250" viewBox="0 0 480 250" aria-hidden="true">
        <polygon fill="var(--paper-shadow)" points="0,14 30,10 60,16 95,8 130,14 170,6 205,12 240,4 280,12 320,6 360,14 400,8 440,14 480,10 480,242 440,236 400,244 360,238 320,246 280,240 240,248 200,240 160,246 120,238 80,244 40,238 0,244"/>
        <polygon fill="var(--paper-cream)" points="0,18 25,12 55,20 90,12 125,18 165,10 200,16 240,8 275,16 315,10 355,18 395,12 435,18 480,14 480,238 440,232 400,240 360,234 320,242 280,236 240,244 200,236 160,242 120,234 80,240 40,234 0,240"/>
      </svg>
      <div class="attic-photo" role="img" aria-label="Black and white photograph of a wooden attic under the roof beams, straw on the floor"></div>
      <div class="portrait-photo" role="img" aria-label="Black and white portrait photograph of a young man in a jacket and tie"></div>
    </div>

    <p class="cover-text publisher-name">Editions Marvolt</p>
  </main>
</body>
</html>
```